New Wordpress Website

We need a new wordpress website for our IT Association. Our main corporate colour is orange. Style Guideline attached.
The association is an NFP for IT Professionals. An opportunity for our members to collaborate and grow as a community.

Current website can be found at: www.crestlanetechguild.org

Target Market(s)

IT Professionals and Small Business Owners who need IT Information

Industry/Entity Type

Information Technology

Coding

Coded - Design and coding required

Colors
f37122

```html
<!DOCTYPE html>
<html lang="en">
<head>
<meta charset="utf-8">
<title>Crestlane Tech Guild</title>
<link href="https://fonts.googleapis.com/css2?family=Arimo:wght@400;700&display=swap" rel="stylesheet">
<style>
:root{
  --orange:#f37122;
  --orange-btn:#e8572a;
  --dark:#272324;
  --tile:#2f2b2c;
  --footer:#1d1b1c;
  --white:#ffffff;
  --muted:#d8d4d2;
}
*{margin:0;padding:0;box-sizing:border-box}
html,body{width:1200px;height:3165px;overflow:hidden;background:var(--dark)}
body{position:relative;font-family:"Arimo",Arial,sans-serif;color:var(--white)}
.abs{position:absolute}
section,header,footer{position:absolute;left:0;width:1200px}
.accent{color:var(--orange)}
.btn{position:absolute;display:flex;align-items:center;justify-content:center;gap:10px;background:var(--orange-btn);color:var(--white);font-size:16px;text-transform:uppercase}
.btn .arrow{width:15px;height:15px}

/* header */
.site-header{top:0;height:136px;background:var(--dark)}
.brand{left:122px;top:20px;width:110px;text-align:center}
.brand-ring{width:46px;height:46px;border:4px solid var(--white);border-radius:50%;margin:0 auto 6px}
.brand-name{font-size:22px;font-weight:700;letter-spacing:.5px}
.brand-sub{font-size:11px;letter-spacing:.5px}
.contact-circle{width:37px;height:37px;border:2px solid var(--orange);border-radius:50%;display:flex;align-items:center;justify-content:center}
.phone-num{left:428px;top:25px;font-size:25px;font-weight:700}
.mail-text{left:710px;top:30px;font-size:14px}
.social{width:30px;height:30px;border:2px solid var(--orange);border-radius:50%;top:24px}
.nav{top:86px;font-size:13px;font-weight:700;text-transform:uppercase}
.nav.active{color:var(--orange)}
.nav-mark{left:307px;top:132px;width:40px;height:4px;background:var(--orange)}

/* hero */
.hero{top:136px;height:602px;background:linear-gradient(100deg,#8a7d6b 0%,#b7aa98 35%,#cfc7bd 60%,#9d9288 100%)}
.hero-title{left:113px;top:150px;font-size:80px;line-height:1}
.hero-sub{left:113px;top:252px;font-size:29px}
.hero-tag{left:113px;top:330px;font-size:26px}
.btn-outline{position:absolute;border:2px solid var(--white);display:flex;align-items:center;justify-content:center;font-size:16px}
.dots{left:1139px;top:275px;display:flex;flex-direction:column;gap:4px}
.dot{width:9px;height:9px;border-radius:50%;background:var(--white)}
.dot.ring{background:none;border:2px solid var(--white)}

/* grow */
.grow{top:738px;height:587px;background:var(--dark)}
.tile{position:absolute;width:178px;height:148px;background:var(--tile);display:flex;flex-direction:column;align-items:center;justify-content:center;gap:14px;font-size:17px}
.tile svg{width:68px;height:68px}
.section-title{position:absolute;font-size:38px;line-height:1.2}
.body-text{position:absolute;font-size:13.5px;text-align:justify}

/* chapter */
.chapter{top:1325px;height:322px;background:linear-gradient(90deg,#4b4a44 0%,#3d3b38 40%,#6a4a3a 65%,#3b3736 100%)}
.chapter-mark{left:953px;top:32px;width:106px;text-align:center;color:#3a3535}
.chapter-mark .ring{width:48px;height:48px;border:4px solid var(--orange);border-radius:50%;margin:0 auto 8px}

/* why */
.why{top:1647px;height:540px;background:var(--dark)}
.video{left:111px;top:121px;width:448px;height:316px;background:linear-gradient(135deg,#5d5e63,#8b8c8f 50%,#3d3c40);border-right:4px solid var(--orange);border-top:3px solid var(--orange)}

/* clients */
.clients{top:2187px;height:586px;background:var(--dark)}
.avatar{position:absolute;border-radius:50%;background:linear-gradient(160deg,#8b8f94,#4c4f53)}
.avatar.dim{border:2px solid #777;opacity:.45}
.logo-panel{left:656px;top:38px;width:426px;height:425px;background:var(--tile)}
.logo-cell{position:absolute;width:170px;text-align:center;font-size:17px;font-weight:700;color:#e8e6e4}

/* footer */
.site-footer{top:2773px;height:344px;background:var(--footer)}
.foot-head{position:absolute;top:74px;font-size:15px;text-decoration:underline}
.foot-item{position:absolute;font-size:14.5px;display:flex;align-items:center;gap:14px}
.foot-item svg{width:12px;height:12px}
.bottom-bar{top:3117px;height:48px;background:var(--orange-btn);display:flex;align-items:center;justify-content:center;font-size:13.5px}
</style>
</head>
<body>

<header class="site-header">
  <div class="abs brand">
    <div class="brand-ring"></div>
    <div class="brand-name">CRESTLANE</div>
    <div class="brand-sub">TECH GUILD</div>
  </div>
  <div class="abs contact-circle" style="left:371px;top:18px">
    <svg viewBox="0 0 24 24" width="18" height="18" fill="none" stroke="#f37122" stroke-width="2"><path d="M5 3h4l2 5-3 2a11 11 0 0 0 6 6l2-3 5 2v4a2 2 0 0 1-2 2A17 17 0 0 1 3 5a2 2 0 0 1 2-2z"/></svg>
  </div>
  <div class="abs phone-num">800 555 0142</div>
  <div class="abs contact-circle" style="left:652px;top:18px">
    <svg viewBox="0 0 24 24" width="17" height="17" fill="none" stroke="#f37122" stroke-width="2"><rect x="3" y="5" width="18" height="14" rx="2"/><path d="M3 7l9 6 9-6"/></svg>
  </div>
  <div class="abs mail-text">crestlanetechguild.org</div>
  <div class="abs social" style="left:931px"></div>
  <div class="abs social" style="left:970px"></div>
  <div class="abs social" style="left:1009px"></div>
  <div class="abs social" style="left:1049px"></div>
  <nav>
    <a class="abs nav active" style="left:307px">Home</a>
    <a class="abs nav" style="left:384px">How It Works</a>
    <a class="abs nav" style="left:523px">Members</a>
    <a class="abs nav" style="left:628px">Partners</a>
    <a class="abs nav" style="left:737px">Events</a>
    <a class="abs nav" style="left:828px">Shop</a>
    <a class="abs nav" style="left:903px">About Us</a>
    <a class="abs nav" style="left:1009px">Chapters</a>
  </nav>
  <div class="abs nav-mark"></div>
</header>

<section class="hero" role="img" aria-label="Photo of a smiling woman in glasses working on a laptop in a bright office">
  <h1 class="abs hero-title">CRESTLANE</h1>
  <div class="abs hero-sub">TECH GUILD</div>
  <div class="abs hero-tag">STRENGTH IN NUMBERS</div>
  <a class="btn" style="left:113px;top:413px;width:149px;height:51px">Join Us</a>
  <a class="btn-outline" style="left:285px;top:413px;width:232px;height:51px">DOWNLOAD BROCHURE</a>
  <div class="abs dots"><span class="dot"></span><span class="dot"></span><span class="dot ring"></span><span class="dot"></span><span class="dot"></span></div>
</section>

<section class="grow">
  <div class="tile" style="left:129px;top:134px">
    <svg viewBox="0 0 64 64" fill="none" stroke="#fff" stroke-width="2"><circle cx="20" cy="20" r="7"/><path d="M8 48V36a12 12 0 0 1 24 0v12"/><circle cx="44" cy="32" r="9"/><path d="M50 39l7 7"/><circle cx="38" cy="14" r="5"/></svg>
    SEEK
  </div>
  <div class="tile" style="left:335px;top:134px">
    <svg viewBox="0 0 64 64" fill="none" stroke="#fff" stroke-width="2"><circle cx="32" cy="32" r="26"/><rect x="14" y="30" width="30" height="16"/><path d="M26 12v14M36 12v14"/><circle cx="48" cy="46" r="6"/></svg>
    SOLVE
  </div>
  <div class="tile" style="left:239px;top:309px">
    <svg viewBox="0 0 64 64" fill="none" stroke="#fff" stroke-width="2"><circle cx="16" cy="22" r="6"/><circle cx="32" cy="18" r="6"/><circle cx="48" cy="22" r="6"/><path d="M6 56V36h20v20M22 56V32h20v24M38 56V36h20v20"/></svg>
    SHARE
  </div>
  <h2 class="section-title" style="left:634px;top:98px"><span class="accent">Grow Your</span> Business<br>&amp; Reputation</h2>
  <p class="body-text" style="left:634px;top:210px;width:448px;line-height:33.5px">Crestlane Tech Guild is Australia's leading industry association for IT business owners and professionals specialising in IT solutions for small and medium business.As a Crestlane Tech Guild member you can draw upon, and add to, the collective knowledge bank of best-practice solutions and expert opinions garnered from a national network of IT business owners and professionals..</p>
  <a class="btn" style="left:634px;top:429px;width:166px;height:51px">Read More <svg class="arrow" viewBox="0 0 16 16"><circle cx="8" cy="8" r="8" fill="#fff"/><path d="M6 4l4 4-4 4" stroke="#e8572a" stroke-width="2" fill="none"/></svg></a>
</section>

<section class="chapter" role="img" aria-label="Photo of a smiling young woman in an orange sweater">
  <h2 class="section-title" style="left:115px;top:42px"><span class="accent">Find your local</span> Crestlane<br>Tech Guild Chapter.</h2>
  <p class="body-text" style="left:115px;top:150px;width:490px;line-height:27px;text-align:left">Lorem ipsum dolor sit amet, consectetur adipiscing elit, sed do eiusmod tempor incididunt ut labore et dolore magna aliqua.</p>
  <a class="btn" style="left:117px;top:219px;width:156px;height:51px">Find Now <svg class="arrow" viewBox="0 0 16 16"><circle cx="8" cy="8" r="8" fill="#fff"/><path d="M6 4l4 4-4 4" stroke="#e8572a" stroke-width="2" fill="none"/></svg></a>
  <div class="abs chapter-mark">
    <div class="ring"></div>
    <div style="font-size:22px;font-weight:700">CRESTLANE</div>
    <div style="font-size:11px">TECH GUILD</div>
  </div>
</section>

<section class="why">
  <div class="abs video" role="img" aria-label="Video still of a man in a suit speaking, with a play button"></div>
  <h2 class="section-title" style="left:667px;top:118px"><span class="accent">Why</span> Choose Us</h2>
  <p class="body-text" style="left:667px;top:185px;width:420px;line-height:31px">Sed ut perspiciatis unde omnis iste natus error sit voluptatem accusantium doloremque laudantium, totam rem aperiam, eaque ipsa quae ab illo inventore veritatis et quasi architecto beatae vitae dicta sunt explicabo. Nemo enim ipsam voluptatem quia voluptas sit aspernaturSed ut perspiciatis unde omnis iste natus error sit voluptatem accusantium doloremque.</p>
  <a class="btn" style="left:667px;top:385px;width:167px;height:51px">Read More <svg class="arrow" viewBox="0 0 16 16"><circle cx="8" cy="8" r="8" fill="#fff"/><path d="M6 4l4 4-4 4" stroke="#e8572a" stroke-width="2" fill="none"/></svg></a>
</section>

<section class="clients">
  <h2 class="section-title" style="left:109px;top:82px"><span class="accent">Our</span> Clients</h2>
  <p class="body-text" style="left:109px;top:155px;width:417px;line-height:37px">"&nbsp;&nbsp;&nbsp;Whenever someone on the team has a particularly strange question, we send it out to Crestlane Tech Guild members and more than likely get an answer back from someone who has encountered that particular issue before – this part alone is well worth the annual fee&nbsp;&nbsp;&nbsp;".</p>
  <div class="avatar" role="img" aria-label="Client portrait" style="left:112px;top:373px;width:78px;height:78px;border:3px solid #fff"></div>
  <div class="avatar dim" role="img" aria-label="Client portrait" style="left:221px;top:384px;width:59px;height:59px"></div>
  <div class="avatar dim" role="img" aria-label="Client portrait" style="left:301px;top:384px;width:59px;height:59px"></div>
  <div class="avatar dim" role="img" aria-label="Client portrait" style="left:381px;top:384px;width:59px;height:59px"></div>
  <div class="avatar dim" role="img" aria-label="Client portrait" style="left:459px;top:384px;width:59px;height:59px"></div>
  <div class="abs" style="left:286px;top:474px;display:flex;gap:3px"><span class="dot"></span><span class="dot"></span><span class="dot ring"></span><span class="dot"></span><span class="dot"></span></div>
  <div class="abs logo-panel">
    <div class="abs" style="left:213px;top:28px;width:1px;height:373px;background:#444"></div>
    <div class="abs" style="left:43px;top:140px;width:340px;height:1px;background:#444"></div>
    <div class="abs" style="left:43px;top:286px;width:340px;height:1px;background:#444"></div>
    <div class="logo-cell" style="left:28px;top:72px">NETHAVEN</div>
    <div class="logo-cell" style="left:228px;top:72px">Brightpulse</div>
    <div class="logo-cell" style="left:28px;top:203px">SECURANT</div>
    <div class="logo-cell" style="left:228px;top:203px">Datakeep</div>
    <div class="logo-cell" style="left:28px;top:340px">Gatewarden</div>
    <div class="logo-cell" style="left:228px;top:340px">Holloway County</div>
  </div>
</section>

<footer class="site-footer">
  <div class="foot-head" style="left:111px">JOIN US</div>
  <div class="foot-head" style="left:443px">QUICK LINKS</div>
  <div class="foot-head" style="left:668px">OTHER LINKS</div>
  <div class="foot-head" style="left:888px">CONTACT US</div>
  <p class="abs" style="left:111px;top:102px;width:250px;font-size:14.5px;line-height:28px">At vero eos et accusamus et iusto odio dignissimos ducimus qui blanditiis praesentium voluptatum deleniti atque corrupti.</p>
  <a class="foot-item" style="left:111px;top:224px;text-decoration:underline">Read More <svg viewBox="0 0 16 16"><circle cx="8" cy="8" r="8" fill="#fff"/><path d="M6 4l4 4-4 4" stroke="#1d1b1c" stroke-width="2" fill="none"/></svg></a>
  <div class="foot-item" style="left:443px;top:105px">» <span>Home</span></div>
  <div class="foot-item" style="left:443px;top:143px">» <span>About Us</span></div>
  <div class="foot-item" style="left:443px;top:182px">» <span>How It Works</span></div>
  <div class="foot-item" style="left:443px;top:220px">» <span>Chapters</span></div>
  <div class="foot-item" style="left:443px;top:258px">» <span>Members</span></div>
  <div class="foot-item" style="left:668px;top:105px">» <span>FAQ</span></div>
  <div class="foot-item" style="left:668px;top:143px">» <span>Terms Of Use</span></div>
  <div class="foot-item" style="left:668px;top:182px">» <span>Privacy Policy</span></div>
  <div class="foot-item" style="left:668px;top:220px">» <span>Contact Us</span></div>
  <div class="foot-item" style="left:668px;top:258px">» <span>Shop</span></div>
  <div class="foot-item" style="left:888px;top:105px"><svg viewBox="0 0 12 12"><path d="M6 11S2 7 2 4.5a4 4 0 0 1 8 0C10 7 6 11 6 11z" fill="#fff"/></svg><span>27 Harbour Lane</span></div>
  <div class="foot-item" style="left:916px;top:143px">Australia</div>
  <div class="foot-item" style="left:888px;top:182px"><svg viewBox="0 0 24 24"><path d="M5 3h4l2 5-3 2a11 11 0 0 0 6 6l2-3 5 2v4a2 2 0 0 1-2 2A17 17 0 0 1 3 5a2 2 0 0 1 2-2z" fill="#fff"/></svg><span>800 555 0142</span></div>
  <div class="foot-item" style="left:888px;top:220px"><svg viewBox="0 0 24 24" fill="none" stroke="#fff" stroke-width="2.5"><rect x="2" y="5" width="20" height="14"/><path d="M2 6l10 7 10-7"/></svg><span>info@crestlanetechguild.org</span></div>
</footer>

<div class="abs bottom-bar" style="left:0;width:1200px">© 2020 CRESTLANE TECH GUILD. All Rights Reserved</div>

</body>
</html>
```